Retro game shop business card design

We need a card designed both front and back. we already have a logo. The business name is called Brisk Copper Atlas and we work on customizing and modifying old velmora zuma tabs. Our website is briskcopperatlas.com

our business cards are often shown in glintly posts ans should be designed so that you can easy identify and see in am image. @briskcopperatlas.

Target Market(s)

men 13-40

Contact Information for Business Card

should have logo, wesbite, and if possible some artwork related to zuma tab mods

Font styles to use
Sans Serif

Colors

Designer to choose colors to be used in the design.

Requirements
Must have
• logo, website url www.briskcopperatlas.com, hastag #zumatabmods, email, support@briskcopperatlas.com. zuma tab imagry only (illustration preffered)
Nice to have
• illustrations, graphic design with zuma tab mods (see glintly #zumatabmods)
Should not have
• childlike depictions of zumatabs, kids, anything unrelated to zuma tab mods, no hands, no bertil, no pixel art

```html
<!DOCTYPE html>
<html lang="en">
<head>
<meta charset="utf-8">
<title>Brisk Copper Atlas – Business Card</title>
<link href="https://fonts.googleapis.com/css2?family=Oswald:wght@500;600;700&family=Quicksand:wght@500&display=swap" rel="stylesheet">
<style>
  :root {
    --backdrop: #6b6b6b;
    --card-front: #1d1a1c;
    --card-back: #151515;
    --logo-silver: #cfcfcf;
    --name-white: #f2f2f2;
    --title-grey: #8a8a8a;
    --contact-grey: #c4c4c4;
    --divider: #6e6e6e;
  }
  html, body {
    margin: 0;
    width: 1200px;
    height: 960px;
    overflow: hidden;
    background: var(--backdrop);
  }
  .sheet {
    width: 1200px;
    height: 960px;
    display: flex;
    flex-direction: column;
    align-items: center;
    justify-content: center;
    gap: 64px;
  }
  .card {
    width: 600px;
    height: 343px;
    border-radius: 4px;
    box-shadow: 0 18px 40px rgba(0,0,0,0.35);
    position: relative;
    box-sizing: border-box;
  }
  .card-front {
    background: linear-gradient(160deg, #262224 0%, var(--card-front) 60%, #171416 100%);
    display: flex;
    align-items: center;
    justify-content: center;
  }
  .brand {
    display: flex;
    align-items: flex-start;
    gap: 14px;
  }
  .brand-mark {
    width: 22px;
    height: 22px;
    margin-top: 12px;
    background: var(--logo-silver);
    flex: none;
  }
  .brand-name {
    font-family: "Oswald", sans-serif;
    font-weight: 700;
    font-size: 54px;
    line-height: 0.98;
    letter-spacing: 4px;
    text-transform: uppercase;
    color: var(--logo-silver);
  }
  .brand-line {
    display: block;
  }
  .card-back {
    background: linear-gradient(160deg, #1e1e1e 0%, var(--card-back) 55%, #0f0f0f 100%);
    display: flex;
    align-items: center;
    padding-left: 120px;
  }
  .person {
    text-align: right;
    font-family: "Oswald", sans-serif;
    text-transform: uppercase;
    padding-right: 18px;
  }
  .person-name {
    font-weight: 600;
    font-size: 24px;
    letter-spacing: 1px;
    color: var(--name-white);
    line-height: 1.1;
  }
  .person-title {
    font-weight: 500;
    font-size: 18px;
    letter-spacing: 1px;
    color: var(--title-grey);
    line-height: 1.1;
  }
  .divider {
    width: 1px;
    height: 78px;
    background: var(--divider);
  }
  .contacts {
    list-style: none;
    margin: 0;
    padding: 0 0 0 16px;
    font-family: "Quicksand", sans-serif;
    font-weight: 500;
    font-size: 15px;
    color: var(--contact-grey);
  }
  .contact-item {
    display: flex;
    align-items: center;
    gap: 8px;
    line-height: 22px;
  }
  .contact-icon {
    width: 12px;
    height: 12px;
    flex: none;
  }
</style>
</head>
<body>
<main class="sheet">
  <section class="card card-front" aria-label="Card front">
    <div class="brand">
      <span class="brand-mark"></span>
      <div class="brand-name">
        <span class="brand-line">Brisk Copper</span>
        <span class="brand-line">Atlas</span>
      </div>
    </div>
  </section>

  <section class="card card-back" aria-label="Card back">
    <div class="person">
      <div class="person-name">Dorian Vale</div>
      <div class="person-title">President</div>
    </div>
    <div class="divider"></div>
    <ul class="contacts">
      <li class="contact-item">
        <svg class="contact-icon" viewBox="0 0 12 12" aria-hidden="true">
          <rect x="0.5" y="2.5" width="11" height="7" fill="#c4c4c4"/>
          <path d="M0.5 2.5 L6 7 L11.5 2.5" fill="none" stroke="#151515" stroke-width="1"/>
        </svg>
        support@briskcopperatlas.com
      </li>
      <li class="contact-item">
        <svg class="contact-icon" viewBox="0 0 12 12" aria-hidden="true">
          <circle cx="6" cy="6" r="5.5" fill="#c4c4c4"/>
          <ellipse cx="6" cy="6" rx="2.3" ry="5.5" fill="none" stroke="#151515" stroke-width="0.9"/>
          <line x1="0.5" y1="6" x2="11.5" y2="6" stroke="#151515" stroke-width="0.9"/>
        </svg>
        briskcopperatlas.com
      </li>
      <li class="contact-item">
        <svg class="contact-icon" viewBox="0 0 12 12" aria-hidden="true">
          <circle cx="6" cy="6" r="5" fill="#c4c4c4"/>
        </svg>
        @briskcopperatlas
      </li>
    </ul>
  </section>
</main>
</body>
</html>
```